innovative investment real estate sales firm

We are a uniquely collabrative firm that seeks to bring a conultative approach to uncovering hidden opportunities for our clients, our website needs to convey our client focused approach. Our firm specializes in the sale of apartment properties in Southern California. We have a team of researchers, transaction coordinators and marketing personal to support our geographically specialized advisers. We need a website that introduces clients to our unique way of better helping them achieve their investment goals.

Target Market(s)

High net worth individuals and families

Industry/Entity Type

Real Estate Agent

Font styles to use
Other font styles liked:
• please use font provided

Requirements
Must have
• Stories of our recent projects
• Features on our people
• email capture for viewing inventory
• content that showcases our unique consultative approach that uncovers unrealized opportunities

```html
<!DOCTYPE html>
<html lang="en">
<head>
<meta charset="utf-8">
<title>Meridian Advisers — Multifamily Properties</title>
<link href="https://fonts.googleapis.com/css2?family=Hind:wght@400;500;600;700&display=swap" rel="stylesheet">
<style>
:root{
  --teal:#14a3b8;
  --green:#8cc81e;
  --slate:#4a5563;
  --slate-dark:#3f4956;
  --mist:#cfe1e1;
  --text:#555f6b;
  --ink:#3a4350;
  --white:#ffffff;
  --topbar:#dedfdf;
  --fb:#3b5a9a;
  --tw:#2ba1dc;
  --gp:#d9483b;
}
*{box-sizing:border-box;margin:0;padding:0}
html,body{width:1200px;height:2883px;overflow:hidden}
body{position:relative;background:var(--white);font-family:"Hind",sans-serif;color:var(--text)}
.abs{position:absolute}
a{color:inherit;text-decoration:none}

.topbar{left:0;top:0;width:1200px;height:20px;background:var(--topbar);font-size:11px;color:#8a939b;display:flex;justify-content:flex-end;align-items:center;gap:14px;padding-right:160px}
.topbar .phone{font-weight:600;color:#6b747c}

.header{left:0;top:20px;width:1200px;height:80px;background:var(--white)}
.brand{left:162px;top:18px;display:flex;align-items:center;gap:12px}
.brand-mark{width:36px;height:36px;background:var(--teal)}
.brand-name{font-size:20px;font-weight:600;color:var(--slate-dark);letter-spacing:1px;line-height:1}
.nav{right:112px;top:36px;display:flex;gap:18px;font-size:12px;font-weight:600;letter-spacing:1.2px;color:var(--ink);text-transform:uppercase}
.nav .active{color:var(--teal)}

.hero{left:0;top:100px;width:1200px;height:426px;background:var(--mist);overflow:hidden}
.hero h1{left:188px;top:140px;font-size:48px;font-weight:600;color:var(--teal);line-height:1}
.hero p{left:188px;top:202px;width:440px;font-size:14px;line-height:26px;color:var(--text)}
.btn-green{left:192px;top:296px;width:174px;height:40px;background:var(--green);color:var(--white);font-size:12px;font-weight:600;letter-spacing:1.5px;display:flex;align-items:center;justify-content:center}
.hero-art{left:640px;top:0;width:560px;height:426px}

.services{left:160px;top:586px;width:880px;display:flex;justify-content:space-between}
.service{width:200px;text-align:center}
.service .icon{width:70px;height:70px;border-radius:50%;background:var(--slate);margin:0 auto 12px;display:flex;align-items:center;justify-content:center}
.service .icon.teal{background:var(--teal)}
.service h3{font-size:14px;font-weight:600;letter-spacing:1.2px;color:var(--ink);line-height:20px;text-transform:uppercase}
.service p{margin-top:10px;font-size:12.5px;line-height:22px;color:var(--text)}

.about-kicker{left:183px;top:884px;font-size:13px;font-weight:700;letter-spacing:2px;color:var(--teal)}
.about-title{left:183px;top:898px;font-size:32px;font-weight:600;color:var(--slate-dark);padding-bottom:4px;border-bottom:3px solid var(--teal);line-height:1.1}
.about-text{left:183px;top:953px;width:410px;font-size:14px;line-height:26px}
.about-photo{left:614px;top:816px;width:586px;height:243px;background:linear-gradient(135deg,#c6d6dc 0%,#f1f3f4 45%,#d9c9a8 75%,#7b7f8a 100%)}

.section-title{left:0;width:1200px;text-align:center}
.section-title span{display:inline-block;font-size:26px;font-weight:600;letter-spacing:1.5px;color:var(--slate-dark);text-transform:uppercase;border-bottom:3px solid var(--teal);padding:0 4px 2px}

.project{overflow:hidden}
.project .photo{width:100%}
.project .label{width:100%;background:var(--slate);color:var(--white);font-size:17px;font-weight:600;display:flex;align-items:center;justify-content:center;letter-spacing:.5px}
.project .label.teal{background:var(--teal)}
.sky-a{background:linear-gradient(180deg,#aac9e0 0%,#d9d3c1 45%,#6f8b4c 80%,#4d6a35 100%)}
.sky-b{background:linear-gradient(180deg,#9fb383 0%,#c5c9c3 45%,#8d9c6b 75%,#5d6e3d 100%)}
.sky-c{background:linear-gradient(180deg,#4f92d8 0%,#9ec4e8 35%,#c48a5c 60%,#6d8b44 100%)}
.sky-d{background:linear-gradient(180deg,#8cb6dc 0%,#e0c9a4 40%,#c6a27c 60%,#6f9a48 100%)}
.sky-e{background:linear-gradient(180deg,#6aa3db 0%,#a9c6e2 25%,#b8916d 55%,#a07c5d 100%)}
.sky-f{background:linear-gradient(180deg,#7fa6c9 0%,#d9c3a3 40%,#b89d7f 65%,#7a9a55 100%)}

.news{top:2089px;width:265px;display:flex;gap:12px}
.news .date{width:56px;height:62px;background:var(--teal);color:var(--white);text-align:center;flex:none;padding-top:4px}
.news .date .day{font-size:30px;font-weight:600;line-height:30px;margin-top:2px}
.news .date .mon{font-size:10px;line-height:10px}
.news h4{font-size:15px;font-weight:600;color:var(--ink);text-transform:uppercase;border-bottom:2px solid var(--slate-dark);padding-bottom:2px;letter-spacing:.3px;line-height:20px}
.news p{margin-top:6px;font-size:12.5px;line-height:21px}

.newsletter{left:0;top:2281px;width:1200px;height:100px;background:var(--teal);color:var(--white)}
.newsletter h5{left:192px;top:28px;font-size:20px;font-weight:600}
.newsletter small{left:192px;top:57px;font-size:12px;font-weight:500}
.newsletter .field{left:624px;top:40px;width:272px;height:36px;background:#4fc0d0;font-size:12px;padding:11px 12px;color:#e6f7fa}
.newsletter .go{left:896px;top:40px;width:120px;height:36px;background:var(--white);color:var(--teal);font-size:12px;font-weight:600;display:flex;align-items:center;justify-content:center;letter-spacing:.5px}

.footer{left:0;top:2381px;width:1200px;height:502px;background:linear-gradient(180deg,#5a6573 0%,#4b5664 50%,#434d5a 100%)}
.contact-card{left:198px;top:2478px;width:272px;height:290px;background:rgba(72,82,95,.85)}
.contact-card .kicker{left:24px;top:60px;font-size:11px;letter-spacing:1.5px;color:#c7cdd3}
.contact-card h6{left:24px;top:76px;font-size:23px;font-weight:600;color:var(--white);letter-spacing:1px;border-bottom:2px solid var(--teal);padding-bottom:1px}
.info{left:24px;display:flex;gap:12px;color:var(--white)}
.info .ic{display:flex;justify-content:center;padding-top:6px;border-right:1px solid #8d96a0;padding-right:10px;width:42px}
.info .lbl{font-size:10px;color:#aeb6be;line-height:14px}
.info .val{font-size:13px;font-weight:600;line-height:19px}
.email-bar{left:198px;top:2768px;width:272px;height:80px;background:#404a57}

.form-title{left:509px;top:2452px;font-size:30px;font-weight:600;letter-spacing:2px;color:var(--white);text-transform:uppercase}
.form-field{height:38px;border-bottom:1px solid #8b949e;color:var(--white);font-size:14px;font-weight:600;display:flex;align-items:center;gap:8px}
.socials{left:893px;top:2704px;display:flex;gap:12px}
.socials span{width:26px;height:26px;border-radius:50%;display:block}
.fnav{left:0;top:2768px;width:1200px;height:115px;background:var(--white)}
.fnav ul{position:absolute;left:502px;top:26px;display:flex;gap:26px;list-style:none;font-size:13px;color:#7c858e}
.fnav li.sep{color:#b5bcc2}
.fnav li.cur{color:var(--ink);font-weight:600}
.copyright{left:505px;top:2836px;font-size:12.5px;font-weight:600;color:var(--ink)}
.copyright b{color:var(--teal);font-weight:600}
</style>
</head>
<body>

<div class="abs topbar"><span>✉ info@meridianadvisers.com</span><span>|</span><span class="phone">☎ 555-201-3344</span></div>

<header class="abs header">
  <div class="abs brand"><span class="brand-mark"></span><span class="brand-name">MERIDIAN ADVISERS</span></div>
  <nav class="abs nav">
    <a class="active">Home</a><a>About ▾</a><a>Investment</a><a>Development</a><a>Properties</a><a>Latest News</a><a>Contact</a>
  </nav>
</header>

<section class="abs hero">
  <h1 class="abs">Lorem ipsum dolor sit</h1>
  <p class="abs">Lorem ipsum dolor sit amet, consectetur adipisicing elit, sed do incididunt ut labore et dolore magna aliqua. Ut enim ad minim nostrudex er citation ullamco laboris nisi ut .</p>
  <a class="abs btn-green">LEARN MORE ›</a>
  <svg class="abs hero-art" viewBox="0 0 560 426" role="img" aria-label="Collage of an adviser presenting a model house, a family outside their new home, a suburban street and a couple reviewing plans">
    <defs>
      <linearGradient id="gMain" x1="0" y1="0" x2="1" y2="1"><stop offset="0" stop-color="#2f3640"/><stop offset=".55" stop-color="#e8ecef"/><stop offset="1" stop-color="#c9b08a"/></linearGradient>
      <linearGradient id="gSmall" x1="0" y1="0" x2="0" y2="1"><stop offset="0" stop-color="#a9c3d8"/><stop offset="1" stop-color="#6f8450"/></linearGradient>
      <linearGradient id="gRight" x1="0" y1="0" x2="1" y2="1"><stop offset="0" stop-color="#eef0f1"/><stop offset="1" stop-color="#b58d6a"/></linearGradient>
    </defs>
    <polygon points="140,0 560,0 560,360 360,426 140,140" fill="url(#gMain)" stroke="#fff" stroke-width="4"/>
    <polygon points="75,290 150,220 240,320 170,400" fill="url(#gSmall)" stroke="#fff" stroke-width="4"/>
    <polygon points="150,426 250,330 330,426" fill="url(#gSmall)" stroke="#fff" stroke-width="4"/>
    <polygon points="370,426 480,320 560,400 560,426" fill="url(#gRight)" stroke="#fff" stroke-width="4"/>
  </svg>
</section>

<section class="abs services">
  <div class="service">
    <div class="icon teal"><svg width="40" height="40" viewBox="0 0 40 40" fill="none" stroke="#fff" stroke-width="2"><path d="M4 20 L18 8 L32 20"/><path d="M8 17 V32 H22"/><circle cx="28" cy="27" r="7"/><path d="M28 23v8M26 25h3a1.5 1.5 0 010 3h-2a1.5 1.5 0 000 3h3"/></svg></div>
    <h3>Property<br>Management</h3>
    <p>Lorem ipsum dolor sit amet, consectetur adipisicing elit, sed eiusmod tempor.</p>
  </div>
  <div class="service">
    <div class="icon"><svg width="40" height="40" viewBox="0 0 40 40" fill="none" stroke="#fff" stroke-width="2"><path d="M12 16 L22 7 L32 16"/><path d="M15 14 V22 H29 V14"/><path d="M4 28 H14 L22 32 L34 26"/><path d="M4 34 H16 L24 36"/></svg></div>
    <h3>Property<br>Investment</h3>
    <p>Lorem ipsum dolor sit amet, consectetur adipisicing elit, sed eiusmod tempor.</p>
  </div>
  <div class="service">
    <div class="icon"><svg width="40" height="40" viewBox="0 0 40 40" fill="none" stroke="#fff" stroke-width="2"><path d="M6 34 H34"/><path d="M8 22 L20 12 L32 22"/><path d="M10 30 L17 24 L22 28 L32 18"/><path d="M27 18 H32 V23"/></svg></div>
    <h3>Unlock Hidden<br>Opportunities</h3>
    <p>Lorem ipsum dolor sit amet, consectetur adipisicing elit, sed eiusmod tempor.</p>
  </div>
  <div class="service">
    <div class="icon"><svg width="40" height="40" viewBox="0 0 40 40" fill="none" stroke="#fff" stroke-width="2"><path d="M5 19 L19 7 L33 19"/><path d="M9 16 V33 H22"/><path d="M14 22 H19 V27 H14Z"/><path d="M25 24 L32 31 L29 34 L22 27Z"/></svg></div>
    <h3>Property<br>Development</h3>
    <p>Lorem ipsum dolor sit amet, consectetur adipisicing elit, sed eiusmod tempor.</p>
  </div>
</section>

<div class="abs about-kicker">ABOUT</div>
<h2 class="abs about-title">MERIDIAN ADVISERS</h2>
<p class="abs about-text">Lorem ipsum dolor sit amet, consectetur adipisicing elit, sed do incididunt ut labore et dolore magna aliqua. Ut enim ad minim nostrudex er citation ullamco laboris nisi ut .</p>
<div class="abs about-photo" role="img" aria-label="Advisers signing papers at a desk beside a model house"></div>

<h2 class="abs section-title" style="top:1132px"><span>Our Recent Projects</span></h2>

<div class="abs project" style="left:0;top:1223px;width:338px;height:265px">
  <div class="photo sky-a" style="height:208px" role="img" aria-label="Two-storey family house with a landscaped front garden"></div>
  <div class="label" style="height:57px">RECENT PROJECT #1</div>
</div>
<div class="abs project" style="left:348px;top:1223px;width:518px;height:334px">
  <div class="photo sky-b" style="height:280px" role="img" aria-label="Single-storey cottage with patio umbrellas and a planted courtyard"></div>
  <div class="label teal" style="height:54px">RECENT PROJECT #2</div>
</div>
<div class="abs project" style="left:876px;top:1223px;width:324px;height:334px">
  <div class="photo sky-c" style="height:280px" role="img" aria-label="Mediterranean-style home with palm trees and a double garage"></div>
  <div class="label" style="height:54px">RECENT PROJECT #3</div>
</div>
<div class="abs project" style="left:0;top:1498px;width:338px;height:407px">
  <div class="photo sky-d" style="height:351px" role="img" aria-label="Stucco house with a tiled roof, green lawn and palm trees"></div>
  <div class="label" style="height:56px">RECENT PROJECT #4</div>
</div>
<div class="abs project" style="left:348px;top:1570px;width:360px;height:335px">
  <div class="photo sky-e" style="height:279px" role="img" aria-label="Two-storey tan stucco house under a blue sky"></div>
  <div class="label" style="height:56px">RECENT PROJECT #5</div>
</div>
<div class="abs project" style="left:718px;top:1570px;width:482px;height:335px">
  <div class="photo sky-f" style="height:279px" role="img" aria-label="Family home with an arched entry, flower beds and a wide driveway"></div>
  <div class="label" style="height:56px">RECENT PROJECT #6</div>
</div>

<h2 class="abs section-title" style="top:1988px"><span>Latest News</span></h2>

<article class="abs news" style="left:198px">
  <div class="date"><svg width="14" height="12" viewBox="0 0 14 12" fill="none" stroke="#fff"><rect x="1" y="2" width="12" height="9"/><path d="M1 5h12"/></svg><div class="day">13</div><div class="mon">July</div></div>
  <div><h4>Lorem Ipsum Dolor</h4><p>Lorem ipsum dolor sit amet, consectetur adipisicing elit, sed eiusmod tempor.</p></div>
</article>
<article class="abs news" style="left:476px">
  <div class="date"><svg width="14" height="12" viewBox="0 0 14 12" fill="none" stroke="#fff"><rect x="1" y="2" width="12" height="9"/><path d="M1 5h12"/></svg><div class="day">11</div><div class="mon">July</div></div>
  <div><h4>A Dipisicing Elit</h4><p>Lorem ipsum dolor sit amet, consectetur adipisicing elit, sed eiusmod tempor.</p></div>
</article>
<article class="abs news" style="left:753px">
  <div class="date"><svg width="14" height="12" viewBox="0 0 14 12" fill="none" stroke="#fff"><rect x="1" y="2" width="12" height="9"/><path d="M1 5h12"/></svg><div class="day">10</div><div class="mon">July</div></div>
  <div><h4>Do Eiusmod Tempor</h4><p>Lorem ipsum dolor sit amet, consectetur adipisicing elit, sed eiusmod tempor.</p></div>
</article>

<section class="abs newsletter">
  <h5 class="abs">Subscribe to our Newsletter</h5>
  <small class="abs">Get healthy news and solutions to your problems from our experts!</small>
  <div class="abs field">Your email address..</div>
  <a class="abs go">SUBSCRIBE ›</a>
</section>

<footer class="abs footer" role="img" aria-label="Faded view of a residential street with houses behind the contact area"></footer>

<div class="abs contact-card">
  <svg class="abs" style="left:24px;top:20px" width="34" height="28" viewBox="0 0 34 28" fill="none" stroke="#fff" stroke-width="1.6"><circle cx="11" cy="9" r="6"/><path d="M1 27c0-6 4-10 10-10s10 4 10 10"/><circle cx="24" cy="8" r="5"/><path d="M22 16c6 0 11 4 11 10"/></svg>
  <div class="abs kicker">GET STARTED NOW</div>
  <h6 class="abs">CONTACT INFO</h6>
  <div class="abs info" style="top:150px">
    <div class="ic"><svg width="20" height="24" viewBox="0 0 20 24" fill="none" stroke="#fff" stroke-width="1.6"><path d="M10 23s8-8 8-13a8 8 0 00-16 0c0 5 8 13 8 13z"/><circle cx="10" cy="10" r="3"/></svg></div>
    <div><div class="lbl">Address:</div><div class="val">48 Harbor Ave<br>Dayton, OH 45402</div></div>
  </div>
  <div class="abs info" style="top:226px">
    <div class="ic"><svg width="22" height="22" viewBox="0 0 22 22" fill="none" stroke="#fff" stroke-width="1.6"><path d="M5 2l4 4-2 3c1 3 3 5 6 6l3-2 4 4-3 3C9 20 2 13 2 5z"/></svg></div>
    <div><div class="lbl">Phone:</div><div class="val">555 201 3344</div></div>
  </div>
</div>

<h2 class="abs form-title">Request an Information</h2>
<div class="abs form-field" style="left:512px;top:2508px;width:240px">◯ First Name</div>
<div class="abs form-field" style="left:766px;top:2508px;width:242px">◯ Last Name</div>
<div class="abs form-field" style="left:512px;top:2566px;width:240px">✆ Phone</div>
<div class="abs form-field" style="left:766px;top:2566px;width:242px">✉ Email</div>
<div class="abs form-field" style="left:512px;top:2618px;width:496px;height:68px;align-items:flex-start;padding-top:10px">✉ Message</div>
<div class="abs socials"><span style="background:var(--fb)"></span><span style="background:var(--tw)"></span><span style="background:var(--gp)"></span></div>

<div class="abs fnav">
  <ul><li class="cur">Home</li><li class="sep">•</li><li>About</li><li class="sep">•</li><li>Investment</li><li class="sep">•</li><li>Development</li><li class="sep">•</li><li>Properties</li><li class="sep">•</li><li>Contact</li></ul>
</div>
<div class="abs copyright">© 2017 <b>Meridian Advisers Multifamily Properties.</b> All rights reserved</div>

<div class="abs email-bar">
  <div class="abs info" style="top:20px;left:24px">
    <div class="ic"><svg width="22" height="16" viewBox="0 0 22 16" fill="none" stroke="#fff" stroke-width="1.6"><rect x="1" y="1" width="20" height="14"/><path d="M1 1l10 8 10-8"/></svg></div>
    <div><div class="lbl">Email:</div><div class="val" style="font-size:12px">info@meridianadvisers.com</div></div>
  </div>
</div>

</body>
</html>
```